Flyer for Addiction program

Hi There,There are two parts to this project.1. A double-sided flyer for my next 5-day treatment program for addictions and family trauma.2. A one-page cover for the front of the course folders to match the above flyer?I have put together an information folder. Here is the boxfolio link;https://www.boxfolio.com/sh/jn7lkly6wcqphpt/AACmad0pag08NeuT2pM27USPa?dl=0Included in the information folder is;1. Copy2. Selection of images3. Logos and Brand identity kit4. Examples of past flyers and folder coverPlease don't hesitate to contact me if you have any questions.RegardsRebecca

Colors

Designer to choose colors to be used in the design.

Requirements
Must have
• 2 pages flyer please.
• Contemporary / fresh design

```html
<!DOCTYPE html>
<html lang="en">
<head>
<meta charset="utf-8">
<title>Changing the Family Script – Folder Covers</title>
<link href="https://fonts.googleapis.com/css2?family=Bebas+Neue&family=Montserrat:wght@400;600;700&display=swap" rel="stylesheet">
<style>
  :root{
    --board:#5f5f5f;
    --board-edge:#4c4c4c;
    --ink-white:#ffffff;
    --ink-navy:#13233f;
    --ink-stone:#a3a098;
    --ink-shadow:#3d3d3d;
    --ink-pale:#d6d6d6;
    --night:#000000;
    --sky-top:#8d7f5c;
    --sky-mid:#c9b37c;
    --sky-glow:#e9d7a0;
    --meadow-top:#7b6a55;
    --meadow-mid:#6f7a4a;
    --meadow-low:#5b7238;
  }
  *{margin:0;padding:0;box-sizing:border-box}
  html,body{width:1200px;height:871px;overflow:hidden}
  body{
    background:radial-gradient(ellipse at 50% 40%,var(--board) 0%,var(--board-edge) 100%);
    font-family:"Montserrat",sans-serif;
    position:relative;
  }
  .cover{
    position:absolute;top:48px;width:516px;height:730px;overflow:hidden;
    box-shadow:0 6px 18px rgba(0,0,0,.45);
  }
  .cover--dusk{left:55px;background:var(--night)}
  .cover--meadow{left:625px;background:var(--ink-navy)}

  .dusk-photo{
    position:absolute;left:0;top:0;width:516px;height:400px;
    background:
      radial-gradient(circle at 15% 88%,rgba(255,245,210,.95) 0,rgba(240,215,150,.6) 12%,rgba(0,0,0,0) 40%),
      linear-gradient(180deg,var(--sky-top) 0%,var(--sky-mid) 45%,var(--sky-glow) 75%,#b79a5c 92%,#1a140a 100%);
  }
  .brand{position:absolute;left:0;width:100%;text-align:center}
  .brand-mark{display:block;margin:0 auto;border-radius:50%}
  .brand-name{line-height:1}
  .cover--dusk .brand{top:44px}
  .cover--dusk .brand-mark{width:78px;height:78px;background:var(--ink-white)}
  .cover--dusk .brand-name{margin-top:62px;color:var(--ink-white);font-size:20px;letter-spacing:5px;font-weight:400}

  .kicker{position:absolute;left:0;width:100%;text-align:center;line-height:1}
  .cover--dusk .kicker{top:423px;color:var(--ink-shadow);font-size:26px;letter-spacing:-.5px}
  .title{position:absolute;left:0;top:0;width:100%;height:100%;font-family:"Bebas Neue",sans-serif;font-weight:400;line-height:1}
  .title-line{display:block;position:absolute;white-space:nowrap}
  .cover--dusk .t1{top:457px;left:121px;font-size:91px;color:var(--ink-white)}
  .cover--dusk .t2{top:532px;left:121px;font-size:77px;color:var(--ink-white)}
  .cover--dusk .t3{top:590px;left:118px;font-size:115px;color:var(--ink-stone)}

  .meadow-top{position:absolute;left:0;top:0;width:516px;height:400px;background:var(--ink-white)}
  .meadow-panel{
    position:absolute;left:19px;top:380px;width:480px;height:332px;background:var(--ink-white);
    border-radius:0 0 12px 12px;
  }
  .meadow-photo{
    position:absolute;left:0;top:0;width:516px;height:380px;
    background:linear-gradient(180deg,var(--meadow-top) 0%,#8a7d68 28%,var(--meadow-mid) 62%,var(--meadow-low) 100%);
    clip-path:polygon(0 0,100% 0,100% 58%,88% 66%,78% 78%,66% 84%,52% 92%,38% 100%,28% 86%,18% 80%,8% 68%,0 66%);
  }
  .cover--meadow .brand{top:404px}
  .cover--meadow .brand-mark{width:54px;height:54px;background:var(--ink-stone)}
  .cover--meadow .brand-name{margin-top:24px;color:var(--ink-navy);font-size:13px;letter-spacing:3px;font-weight:600}
  .cover--meadow .kicker{top:509px;color:var(--ink-pale);font-size:25px;font-weight:700;letter-spacing:-.5px}
  .cover--meadow .t1,.cover--meadow .t3{left:0;width:100%;text-align:center}
  .cover--meadow .t1{top:551px;font-size:46px;color:var(--ink-navy)}
  .cover--meadow .t3{top:590px;font-size:119px;color:var(--ink-stone)}

  .caption{
    position:absolute;top:808px;width:520px;text-align:center;color:var(--ink-white);
    font-size:30px;font-weight:400;line-height:1.2;
  }
  .caption--left{left:53px}
  .caption--right{left:623px}
</style>
</head>
<body>
  <section class="cover cover--dusk">
    <div class="dusk-photo" role="img" aria-label="Silhouette of a family at sunset: a child on a bike with balloons, parents tossing a toddler in the air, a pram"></div>
    <div class="brand">
      <span class="brand-mark"></span>
      <p class="brand-name">LUMEN CIRCLE</p>
    </div>
    <p class="kicker">5 DAY PROGRAM</p>
    <h1 class="title">
      <span class="title-line t1">CHANGING</span>
      <span class="title-line t2">THE FAMILY</span>
      <span class="title-line t3">SCRIPT</span>
    </h1>
  </section>

  <section class="cover cover--meadow">
    <div class="meadow-top"></div>
    <div class="meadow-panel"></div>
    <div class="meadow-photo" role="img" aria-label="Collage of boots on a trail, old family photographs held in a hand, a campfire, and a family walking hand in hand through a meadow"></div>
    <div class="brand">
      <span class="brand-mark"></span>
      <p class="brand-name">LUMEN CIRCLE</p>
    </div>
    <p class="kicker">5 DAY PROGRAM</p>
    <h1 class="title">
      <span class="title-line t1">CHANGING THE FAMILY</span>
      <span class="title-line t3">SCRIPT</span>
    </h1>
  </section>

  <p class="caption caption--left">Folder Cover Sample 3</p>
  <p class="caption caption--right">Folder Cover Sample 4</p>
</body>
</html>
```